Brenvik Innovations
Professional
Daniel Marlow
CEO
5812-4 Calloway Ave #2267
Houston, TX 77194
Daniel@BrenvikInnovations.com
BrenvikInnovations.com
Feel free to play with the function of the business card if possible as seen in: http://www.trelvaform-studio.com/blog/wp-content/uploads/2009/12/lock-picking-business-card.jpg. Card can be paper plastic or metal.
Our company specializes in artificial intelligence, Unmanned aerial vehicles human-machine interfaces and lasers. Please keep this in mind in your designs.
surprise me, I will refine my requirement here after I see a few submissions.
Here are the business logo files

```html
<!DOCTYPE html>
<html lang="en">
<head>
<meta charset="utf-8">
<title>Brenvik Innovations – Business Card</title>
<link href="https://fonts.googleapis.com/css2?family=Source+Sans+3:wght@400;600&display=swap" rel="stylesheet">
<style>
  :root {
    --backdrop: #393939;
    --card-front: #ffffff;
    --card-back: #5b5b5d;
    --brand-purple: #3f3c7e;
    --text-grey: #6a6a6a;
    --text-light: #ffffff;
    --mark-area-tone: #e4e4e6;
    --disc-light: #d9d9db;
  }
  html, body {
    margin: 0;
    padding: 0;
    width: 1200px;
    height: 901px;
    overflow: hidden;
    background: var(--backdrop);
    font-family: "Source Sans 3", "Helvetica Neue", Arial, sans-serif;
  }
  .canvas {
    position: relative;
    width: 1200px;
    height: 901px;
  }
  .card {
    position: absolute;
    left: 238px;
    width: 724px;
    overflow: hidden;
  }
  .card--front {
    top: 21px;
    height: 414px;
    background: var(--card-front);
  }
  .card--back {
    top: 467px;
    height: 408px;
    background: var(--card-back);
  }

  /* Front */
  .mark-area {
    position: absolute;
    left: 0;
    top: 0;
    width: 300px;
    height: 414px;
    background: linear-gradient(90deg, var(--mark-area-tone) 0%, var(--mark-area-tone) 45%, rgba(255,255,255,0) 100%);
  }
  .brand-dot {
    position: absolute;
    left: 170px;
    top: 80px;
    width: 96px;
    height: 96px;
  }
  .brand-name {
    position: absolute;
    left: 290px;
    top: 104px;
    margin: 0;
    font-weight: 600;
    color: var(--brand-purple);
    line-height: 1;
  }
  .brand-name__first {
    display: block;
    font-size: 60px;
    letter-spacing: 1px;
  }
  .brand-name__second {
    display: block;
    margin-top: 4px;
    font-size: 27px;
    letter-spacing: 5px;
  }
  .contact {
    position: absolute;
    left: 292px;
    top: 242px;
    color: var(--text-grey);
    font-size: 16px;
    line-height: 1;
  }
  .contact__person {
    margin: 0 0 18px;
    font-size: 19px;
  }
  .contact__person .person-name { color: var(--brand-purple); }
  .contact__address {
    margin: 0 0 10px;
    font-style: normal;
    line-height: 24px;
  }
  .contact__lines {
    margin: 0;
    display: grid;
    grid-template-columns: 52px auto;
    row-gap: 11px;
  }
  .contact__lines dt, .contact__lines dd { margin: 0; }

  /* Back */
  .brand-disc {
    position: absolute;
    left: 120px;
    top: 150px;
    width: 100px;
    height: 100px;
  }
  .web-address {
    position: absolute;
    left: 340px;
    top: 178px;
    margin: 0;
    font-size: 37px;
    font-weight: 400;
    line-height: 1;
    color: var(--text-light);
  }
</style>
</head>
<body>
<main class="canvas">
  <section class="card card--front" aria-label="Card front">
    <div class="mark-area" role="img" aria-label="Large brand mark decoration"></div>
    <svg class="brand-dot" viewBox="0 0 96 96" aria-hidden="true">
      <circle cx="48" cy="48" r="46" fill="var(--brand-purple)"/>
    </svg>
    <h1 class="brand-name">
      <span class="brand-name__first">Brenvik</span>
      <span class="brand-name__second">Innovations</span>
    </h1>
    <div class="contact">
      <p class="contact__person"><span class="person-name">Daniel Marlow</span> | CEO</p>
      <address class="contact__address">5812-4 Calloway Ave #2267<br>Houston, TX 77194</address>
      <dl class="contact__lines">
        <dt>Cell</dt><dd>:&nbsp; 214-555-0148</dd>
        <dt>Email</dt><dd>:&nbsp; Daniel@BrenvikInnovations.com</dd>
        <dt>Web</dt><dd>:&nbsp; BrenvikInnovations.com</dd>
      </dl>
    </div>
  </section>

  <section class="card card--back" aria-label="Card back">
    <svg class="brand-disc" viewBox="0 0 100 100" aria-hidden="true">
      <circle cx="50" cy="50" r="48" fill="var(--disc-light)"/>
    </svg>
    <p class="web-address">BrenvikInnovations.com</p>
  </section>
</main>
</body>
</html>
```